Torvelin Business Card

We need a business card design. We have a logo from a previous PixelHarbor project and I am attaching the logo files in jpeg and photoshop.

Business

```html
<!DOCTYPE html>
<html lang="en">
<head>
<meta charset="UTF-8">
<title>Torvelin Business Card</title>
<link rel="stylesheet" href="https://fonts.googleapis.com/css2?family=Lato:wght@300;400;700&display=swap">
<style>
  :root {
    --stage: #626262;
    --card-light: #ffffff;
    --card-dark: #1c1c1c;
    --brand-green: #3fb53f;
    --brand-ink: #3b3b3b;
    --text-light: #f2f2f2;
    --text-muted: #d6d6d6;
  }
  * { margin: 0; padding: 0; box-sizing: border-box; }
  html, body {
    width: 1200px;
    height: 900px;
    overflow: hidden;
    background: var(--stage);
    font-family: "Lato", sans-serif;
  }
  .stage {
    width: 1200px;
    height: 900px;
    display: flex;
    align-items: center;
    justify-content: center;
  }
  .business-card {
    width: 900px;
    height: 514px;
    border-radius: 30px;
    overflow: hidden;
    background: var(--card-dark);
    position: relative;
    box-shadow: 0 18px 40px rgba(0, 0, 0, 0.35);
    display: flex;
    flex-direction: column;
  }
  .card-top {
    height: 205px;
    flex: none;
    background: var(--card-light);
    display: flex;
    align-items: center;
    justify-content: center;
    gap: 20px;
    padding-top: 10px;
  }
  .brand-square {
    width: 48px;
    height: 48px;
    background: var(--brand-green);
  }
  .brand-name {
    font-weight: 700;
    font-size: 76px;
    letter-spacing: -1px;
    color: var(--brand-ink);
    line-height: 1;
  }
  .accent-stripe {
    height: 11px;
    flex: none;
    background: var(--brand-green);
  }
  .card-bottom {
    flex: 1;
    padding: 26px 0 0 68px;
    color: var(--text-light);
  }
  .person-name {
    font-size: 40px;
    font-weight: 300;
    line-height: 1.1;
  }
  .person-name strong { font-weight: 700; }
  .person-title {
    font-size: 19px;
    color: var(--text-muted);
    margin-top: 4px;
  }
  .contact-list {
    list-style: none;
    margin-top: 22px;
  }
  .contact-item {
    display: flex;
    align-items: center;
    gap: 16px;
    font-size: 23px;
    line-height: 33px;
    white-space: nowrap;
  }
  .contact-icon {
    width: 20px;
    height: 20px;
    flex: none;
    fill: var(--brand-green);
    stroke: var(--brand-green);
  }
</style>
</head>
<body>
<main class="stage">
  <article class="business-card">
    <header class="card-top">
      <span class="brand-square"></span>
      <span class="brand-name">Torvelin</span>
    </header>
    <div class="accent-stripe"></div>
    <section class="card-bottom">
      <h1 class="person-name">John <strong>Smith</strong></h1>
      <p class="person-title">Title goes here</p>
      <ul class="contact-list">
        <li class="contact-item">
          <svg class="contact-icon" viewBox="0 0 24 24" stroke-width="0"><path d="M3 9c0-3 4-5 9-5s9 2 9 5l-4 2-2-3H9L7 11 3 9z"/><rect x="5" y="12" width="14" height="9" rx="2"/></svg>
          <span>123-456-7890</span>
        </li>
        <li class="contact-item">
          <svg class="contact-icon" viewBox="0 0 24 24" stroke-width="0"><path d="M2 5h20v14H2z"/><path d="M2 5l10 8 10-8" fill="none" stroke="#1c1c1c" stroke-width="2"/></svg>
          <span>yourdomain.com</span>
        </li>
        <li class="contact-item">
          <svg class="contact-icon" viewBox="0 0 24 24" fill="none" stroke-width="2.6" stroke-linecap="round"><path d="M10 14l4-4"/><path d="M8 11l-3 3a3 3 0 0 0 5 5l3-3"/><path d="M16 13l3-3a3 3 0 0 0-5-5l-3 3"/></svg>
          <span>yourname@yourdomain.com</span>
        </li>
        <li class="contact-item">
          <svg class="contact-icon" viewBox="0 0 24 24" stroke-width="0"><path d="M12 3l10 9h-3v9h-5v-6h-4v6H5v-9H2z"/></svg>
          <span>Street address goes here, Suite #303, Alt Bldg, NY 82365</span>
        </li>
      </ul>
    </section>
  </article>
</main>
</body>
</html>
```